Micro Brewery Needs Generic Box Design

We need packaging artwork design for a beer box for small brewery located in the Kingdom of Tonga. We currently have two separate boxes for our flagship brands 'Tidecrest' & 'Melahu' (Tongan for Tidecrest).
The brewery is named 'The Tidecrest Brewery'. With premium new value add products using locally grown Vanilla, Ginger & Mango coming soon we require a generic box that can represent our Brewery and Tonga while reducing the costs involved in having artwork for each product line.
I have loaded files of our current box images. Please feel free to adapt from these or discard altogether.
All our products will be produced at 5% Alc/Vol and will contain 24 Bottles per box so these items should remain in the design layout.
Brewery

```html
<!DOCTYPE html>
<html lang="en">
<head>
<meta charset="utf-8">
<title>The Tidecrest Brewery – 24 Bottle Carton Dieline</title>
<link href="https://fonts.googleapis.com/css2?family=Arvo&family=Courier+Prime&family=Oswald:wght@500;700&display=swap" rel="stylesheet">
<style>
  :root {
    --paper: #ece4d2;
    --board: #4f3520;
    --board-edge: #3f2a18;
    --amber: #a96b2c;
    --amber-deep: #2e1c0e;
    --cream: #efe6d2;
    --blue: #8ea3c9;
    --white: #ffffff;
    --isle: rgba(200, 180, 160, 0.45);
  }
  * { margin: 0; padding: 0; box-sizing: border-box; }
  html, body { width: 1200px; height: 1000px; overflow: hidden; }
  body { background: var(--paper); position: relative; font-family: "Courier Prime", monospace; }

  .dieline { position: absolute; inset: 0; }
  .panel { position: absolute; background: var(--board); box-shadow: 0 1px 2px rgba(0,0,0,.25); }
  .glue-tab { position: absolute; left: 22px; top: 392px; width: 32px; height: 222px; }

  .face-band {
    position: absolute; left: 0; right: 0; top: 113px; height: 227px;
    background: radial-gradient(ellipse at 50% 45%, var(--amber) 0%, #7a4a20 50%, var(--amber-deep) 100%);
  }

  .isles { position: absolute; background: var(--isle); border-radius: 40% 55% 45% 50%; }

  .brand { position: absolute; text-align: center; color: var(--cream); font-family: "Arvo", serif; font-weight: 400; line-height: 1; }
  .brand span { display: block; }
  .brand.on-dark { color: #1d140c; }

  .made-in { position: absolute; text-align: center; color: var(--cream); }
  .made-in.sans { font-family: "Oswald", sans-serif; font-weight: 500; font-size: 10px; color: var(--white); }
  .made-in.mono { font-family: "Courier Prime", monospace; font-size: 13px; letter-spacing: 2px; }

  .count { position: absolute; text-align: center; font-family: "Oswald", sans-serif; line-height: 1; }
  .count b { display: block; font-weight: 700; }
  .count i { display: block; font-style: normal; font-size: 6px; font-weight: 700; }
  .count small { display: block; font-size: 4px; }
  .count.blue b { color: var(--blue); }
  .count.blue i, .count.blue small { color: var(--white); }
  .count.white { color: var(--white); }

  .range { position: absolute; list-style: none; color: var(--cream); font-size: 9px; line-height: 12px; }
  .range li { position: relative; padding-left: 12px; letter-spacing: .3px; }
  .range li::before { content: ""; position: absolute; left: 0; top: 2px; width: 8px; height: 8px; background: var(--white); }
</style>
</head>
<body>
<main class="dieline">

  <svg class="glue-tab" viewBox="0 0 32 222" aria-hidden="true">
    <polygon points="32,0 0,8 0,214 32,222" fill="var(--board)"/>
  </svg>

  <!-- Front panel -->
  <section class="panel" style="left:52px;top:275px;width:333px;height:453px;">
    <div class="brand" style="left:0;right:0;top:26px;">
      <span style="font-size:15px;letter-spacing:3px;">THE</span>
      <span style="font-size:22px;margin-top:3px;">TIDECREST</span>
      <span style="font-size:14px;letter-spacing:3px;margin-top:3px;">BREWERY</span>
    </div>
    <div class="made-in sans" style="left:0;right:0;top:94px;">MADE IN TONGA</div>
    <div class="count blue" style="left:283px;top:10px;"><b style="font-size:22px;">24</b><i>BOTTLES</i><small>330ml</small></div>

    <div class="face-band">
      <div class="isles" role="img" aria-label="Silhouette map of the Tongan islands" style="left:33px;top:18px;width:262px;height:186px;"></div>
      <div class="brand" style="left:0;right:0;top:72px;color:var(--cream);">
        <span style="font-size:22px;letter-spacing:4px;">THE</span>
        <span style="font-size:36px;margin-top:6px;">TIDECREST</span>
        <span style="font-size:21px;letter-spacing:4px;margin-top:6px;">BREWERY</span>
      </div>
      <div class="made-in mono" style="left:0;right:0;top:204px;">MADE IN TONGA</div>
      <div class="count white" style="left:287px;top:12px;"><b style="font-size:22px;">24</b><i>BOTTLES</i><small>330ml</small></div>
    </div>
  </section>

  <!-- Side panel -->
  <section class="panel" style="left:388px;top:222px;width:222px;height:560px;">
    <ul class="range" style="left:149px;top:180px;"><li>TIDECREST</li><li>MELAHU</li><li>SPARKLING<br>WATER</li></ul>
    <div class="isles" role="img" aria-label="Silhouette map of the Tongan islands" style="left:12px;top:228px;width:196px;height:130px;"></div>
    <div class="brand" style="left:0;right:0;top:281px;">
      <span style="font-size:13px;letter-spacing:3px;">THE</span>
      <span style="font-size:20px;margin-top:2px;">TIDECREST</span>
      <span style="font-size:13px;letter-spacing:3px;margin-top:2px;">BREWERY</span>
    </div>
    <div class="count blue" style="left:8px;top:352px;"><b style="font-size:22px;">24</b><i>BOTTLES</i><small>330ml</small></div>
  </section>

  <!-- Back panel -->
  <section class="panel" style="left:613px;top:275px;width:334px;height:453px;">
    <ul class="range" style="left:12px;top:38px;"><li>TIDECREST</li><li>MELAHU</li><li>SPARKLING<br>WATER</li></ul>
    <div class="brand" style="left:0;right:0;top:26px;padding-left:30px;">
      <span style="font-size:15px;letter-spacing:3px;">THE</span>
      <span style="font-size:22px;margin-top:3px;">TIDECREST</span>
      <span style="font-size:14px;letter-spacing:3px;margin-top:3px;">BREWERY</span>
    </div>
    <div class="made-in sans" style="left:30px;right:0;top:94px;">MADE IN TONGA</div>
    <div class="count blue" style="left:285px;top:10px;"><b style="font-size:22px;">24</b><i>BOTTLES</i><small>330ml</small></div>

    <div class="face-band">
      <div class="isles" role="img" aria-label="Silhouette map of the Tongan islands" style="left:33px;top:18px;width:262px;height:186px;"></div>
      <div class="brand" style="left:0;right:0;top:72px;">
        <span style="font-size:22px;letter-spacing:4px;">THE</span>
        <span style="font-size:36px;margin-top:6px;">TIDECREST</span>
        <span style="font-size:21px;letter-spacing:4px;margin-top:6px;">BREWERY</span>
      </div>
      <div class="made-in mono" style="left:0;right:0;top:204px;">MADE IN TONGA</div>
      <div class="count white" style="left:287px;top:12px;"><b style="font-size:22px;">24</b><i>BOTTLES</i><small>330ml</small></div>
    </div>
  </section>

  <!-- Second side panel -->
  <section class="panel" style="left:950px;top:222px;width:222px;height:560px;">
    <ul class="range" style="left:149px;top:180px;"><li>TIDECREST</li><li>MELAHU</li><li>SPARKLING<br>WATER</li></ul>
    <div class="isles" role="img" aria-label="Silhouette map of the Tongan islands" style="left:12px;top:228px;width:196px;height:130px;"></div>
    <div class="brand" style="left:0;right:0;top:281px;">
      <span style="font-size:13px;letter-spacing:3px;">THE</span>
      <span style="font-size:20px;margin-top:2px;">TIDECREST</span>
      <span style="font-size:13px;letter-spacing:3px;margin-top:2px;">BREWERY</span>
    </div>
    <div class="count blue" style="left:8px;top:352px;"><b style="font-size:22px;">24</b><i>BOTTLES</i><small>330ml</small></div>
  </section>

</main>
</body>
</html>
```